Wordpress Site Design for a Horror and Action Movie Production Company

We need a re-design/facelift of our website: https://q7zk.pagecraftr-demo.net
The structure of the website could remain the same, but it needs to look and feel BETTER!

We would like the website coded in Wordpress so that it can be easily updated bu us, via adding new projects and new projects' info.

We specialize in Action, Horror, and Sci-Fi Genre. That being said, we don't want the website to look like it's a themed park with haunted houses. It should still be sharp and professional, as after all - it is a business for us!

Target Market(s)

Film Distribution Companies (B2B), as well as general audience that likes movies

Industry/Entity Type

Movie Production

Coding

Coded - Design and coding required

Number of Pages Required

5+ page

Font styles to use
Sans Serif

Colors

Designer to choose colors to be used in the design.

Requirements
Must have
• - PROJECTS page
• - Each PROJECT has a sub-page with project info/updates (up dates could be in a form of a WP post, ideally a template that we can use to update and create new PROJECT pages, with text, poster, and video link (trailer))
• - NEWS page that chronologically lists updates from all PROJECTS (could be done via WP blog)
• - HOME page would
Nice to have
• Should generally have a dark background.
• Websites we like as a reference of general approach and style:
• https://marlowvexla.com
• https://tuvakreel.com (however this is very image-centric, and we might not have that much imagery at the moment)
• https://www.pebblecreeklightandframe.com/other
• https://kelvapics.com
Should not have
• We specialize in Action, Horror, and Sci-Fi Genre. That being said, we don't want the website to look like it's a themed park with haunted houses. It should still be sharp and professional, as after all - it is a business for us!

```html
<!DOCTYPE html>
<html lang="en">
<head>
<meta charset="utf-8">
<title>Vantage 9 Pictures</title>
<link href="https://fonts.googleapis.com/css2?family=Montserrat:wght@200;300;400;500;600;700&family=Oswald:wght@400;500&display=swap" rel="stylesheet">
<style>
:root{
  --wine:#1e0204;
  --white:#ffffff;
  --muted:#b79c9e;
  --ink:#1e0204;
  --rule:rgba(255,255,255,.25);
  --box:#d9d4d4;
  --caption:#7d7374;
}
*{margin:0;padding:0;box-sizing:border-box}
html,body{width:1200px;height:2705px;overflow:hidden}
body{font-family:'Montserrat',sans-serif;background:var(--wine);color:var(--white);position:relative}
.abs{position:absolute}

/* hero */
.hero{position:absolute;left:0;top:0;width:1200px;height:720px;overflow:hidden}
.hero-still{position:absolute;inset:0;background:
  radial-gradient(ellipse at 25% 45%,#7a5a48 0%,#4a3226 35%,transparent 60%),
  radial-gradient(ellipse at 80% 40%,#6b4a34 0%,#3e2a1e 40%,transparent 65%),
  linear-gradient(90deg,#3a2a20,#2a1c14 50%,#4a3424)}
.hero-shade{position:absolute;inset:0;background:rgba(20,8,6,.35)}
.grid-line{position:absolute;top:0;width:1px;height:720px;background:var(--rule)}
.brand{left:60px;top:44px;font-weight:700;font-size:20px;letter-spacing:1px;display:flex;align-items:center;gap:8px}
.brand .dot{width:12px;height:12px;border-radius:50%;background:var(--white)}
.brand small{display:block;font-size:7px;letter-spacing:3px;text-align:center;font-weight:600}
.nav-projects{left:959px;top:50px;font-family:'Oswald',sans-serif;font-size:15px;letter-spacing:3px}
.plus-btn{left:1060px;top:40px;width:40px;height:40px;border-radius:50%;background:var(--white)}
.burger{left:108px;top:232px}
.hero-title{left:0;width:1200px;top:312px;text-align:center;font-weight:700;font-size:48px;letter-spacing:11px;padding-left:11px}
.hero-sub{left:0;width:1200px;top:372px;text-align:center;font-weight:600;font-size:24px}
.follow{left:112px;top:600px;transform:rotate(-90deg);transform-origin:left top;font-family:'Oswald',sans-serif;font-size:13px;letter-spacing:3px}
.pager{top:652px;font-family:'Oswald',sans-serif;font-size:15px;letter-spacing:3px}

/* about */
.lead{left:240px;width:720px;top:830px;text-align:center;font-size:25px;line-height:36px;font-weight:400}
.lead b{font-weight:700}
.divider{left:360px;top:1005px;width:480px;height:1px;background:rgba(255,255,255,.55)}
.copy{left:239px;width:722px;font-size:15px;line-height:24px;color:var(--muted);text-align:justify;font-weight:400}
.copy b{color:var(--white);font-weight:500}
.founder{top:1265px;width:240px;height:240px;overflow:hidden}
.founder .photo{position:absolute;inset:0}
.founder.active{box-shadow:0 12px 30px rgba(0,0,0,.6)}
.founder .name{position:absolute;left:14px;bottom:26px;transform:rotate(-90deg);transform-origin:left bottom;white-space:nowrap;line-height:1}
.founder .name strong{display:block;font-size:26px;font-weight:700}
.founder .name span{display:block;font-size:14px;font-weight:700;margin-top:2px}

/* partners */
.partners{left:0;top:1625px;width:1200px;height:480px;background:var(--white)}
.partners h2{position:absolute;left:240px;top:190px;color:var(--ink);font-size:26px;line-height:36px;font-weight:700}
.partner-box{position:absolute;top:120px;width:240px;height:240px;border:1px solid var(--box);display:flex;align-items:center;justify-content:center;gap:8px;color:var(--ink);font-weight:700;font-size:16px}
.partner-box .mark{width:18px;height:18px;background:var(--ink)}
.partner-cap{position:absolute;top:374px;width:240px;text-align:center;color:var(--caption);font-size:10px;letter-spacing:1.5px;line-height:14px}

/* contact */
.talk{left:60px;top:2220px;font-family:'Oswald',sans-serif;font-size:25px;letter-spacing:5px;font-weight:400}
.social{left:1024px;top:2225px;display:flex;gap:18px}
.social i{width:14px;height:14px;border-radius:50%;background:var(--white);display:block}
.genres{left:60px;top:2280px;font-size:52px;line-height:64px;font-weight:200}
.cta{left:60px;top:2470px;width:128px;padding:0 0 12px 17px;font-size:15px;border-bottom:1px solid var(--white)}
.legal{left:60px;top:2598px;font-size:12px;font-weight:600;letter-spacing:1px}
.notice{right:60px;top:2598px;font-size:12px;color:var(--muted)}
</style>
</head>
<body>

<header class="hero">
  <div class="hero-still" role="img" aria-label="Film still from the Nightfall trailer: two characters talking in a dim room"></div>
  <div class="hero-shade"></div>
  <div class="grid-line" style="left:240px"></div>
  <div class="grid-line" style="left:480px"></div>
  <div class="grid-line" style="left:720px"></div>
  <div class="grid-line" style="left:960px"></div>

  <div class="abs brand"><span class="dot"></span><div>VANTAGE 9<small>PICTURES</small></div></div>
  <div class="abs nav-projects">PROJECTS</div>
  <svg class="abs plus-btn" viewBox="0 0 40 40"><circle cx="20" cy="20" r="20" fill="#fff"/><path d="M20 12v16M12 20h16" stroke="#1e0204" stroke-width="2"/></svg>
  <svg class="abs burger" width="24" height="18" viewBox="0 0 24 18"><path d="M0 2h24M0 9h24M0 16h24" stroke="#fff" stroke-width="2.4"/></svg>

  <h1 class="abs hero-title">NIGHTFALL</h1>
  <p class="abs hero-sub">Movie Trailer</p>
  <div class="abs follow">FOLLOW US</div>

  <svg class="abs" style="left:112px;top:653px" width="16" height="14" viewBox="0 0 16 14"><path d="M15 7H2M7 1L1 7l6 6" fill="none" stroke="#fff" stroke-width="1.6"/></svg>
  <div class="abs pager" style="left:213px">PRE</div>
  <svg class="abs" style="left:590px;top:647px" width="20" height="18" viewBox="0 0 20 18"><rect x="0" y="8" width="5" height="10" fill="#fff"/><rect x="7" y="0" width="5" height="18" fill="#fff"/><rect x="14" y="5" width="5" height="13" fill="#fff"/></svg>
  <div class="abs pager" style="left:959px">NEX</div>
  <svg class="abs" style="left:1072px;top:653px" width="16" height="14" viewBox="0 0 16 14"><path d="M1 7h13M9 1l6 6-6 6" fill="none" stroke="#fff" stroke-width="1.6"/></svg>
</header>

<section class="about">
  <p class="abs lead"><b>Vantage 9 Pictures</b> is a fresh brand of multi- media entertainment, aimed at development of original Canadian content as well as servicing of foreign productions in Toronto, Ontario, Canada.</p>
  <div class="abs divider"></div>
  <p class="abs copy" style="top:1040px">We produce genre feature films, series, documentaries, and anything else that we feel great about. <b>We take pride in our innovative approach to the process of filmmaking and marketing of our produced content</b>. In simple terms, we make good looking motion picture content that is entertaining, visually compelling, and tells a good story.</p>
  <p class="abs copy" style="top:1160px">The decades of <b>combined experience of the 4 founders</b> of Vantage 9 Pictures provide an unparalleled expertise of storytelling, production, sales and marketing of films.</p>

  <div class="abs founder" style="left:60px">
    <div class="photo" role="img" aria-label="Portrait of founder Dorian Vale" style="background:linear-gradient(160deg,#cfadb0,#9a7276 60%,#3a2224)"></div>
    <div class="name"><strong>Dorian</strong><span>Vale</span></div>
  </div>
  <div class="abs founder active" style="left:340px">
    <div class="photo" role="img" aria-label="Portrait of founder Tobin Raske" style="background:linear-gradient(180deg,#d4d4d4 0%,#bdbdbd 60%,#2aa0cf 82%,#2aa0cf)"></div>
    <div class="name" style="color:#1e0204"><strong>Tobin</strong><span>Raske</span></div>
  </div>
  <div class="abs founder" style="left:620px">
    <div class="photo" role="img" aria-label="Portrait of founder Marco Selt" style="background:linear-gradient(160deg,#c8a7aa,#8d6468 55%,#2c1618)"></div>
    <div class="name"><strong>Marco</strong><span>Selt</span></div>
  </div>
  <div class="abs founder" style="left:900px">
    <div class="photo" role="img" aria-label="Portrait of founder Elias Varn" style="background:linear-gradient(160deg,#d6b6b9,#b08d91 60%,#e6d6d8)"></div>
    <div class="name"><strong>Elias</strong><span>Varn</span></div>
  </div>
</section>

<section class="abs partners">
  <h2>We Proud<br>is Quality of<br>Partners</h2>
  <div class="partner-box" style="left:480px"><span class="mark"></span>EMBER LANE</div>
  <div class="partner-box" style="left:719px">GREY HARBOR</div>
  <p class="partner-cap" style="left:480px">EMBER LANE<br>STUDIOS INC</p>
  <p class="partner-cap" style="left:719px">GREY HARBOR<br>FILMS INC</p>
</section>

<footer>
  <h2 class="abs talk">LET'S TALK ABOUT YOUR PROJECT</h2>
  <div class="abs social" aria-label="Social links"><i></i><i></i><i></i><i></i></div>
  <p class="abs genres">We specialize in Action, Horror,<br>and Sci-Fi Genre.</p>
  <div class="abs cta">Get in Touch</div>
  <p class="abs legal">© 2019 VANTAGE 9 PICTURES INC.</p>
  <p class="abs notice">Script &amp; Story Submission Notice</p>
</footer>

</body>
</html>
```